Business Cards for a Firearms Business - Quorvane Works

Quorvane Works manufactures, distributes and retails firearms parts. I am looking for someone to use the logos that I have provided to design some business cards that show that we're a modern, industrial, design focused and tactical business.

These will be a standard business card on standard cardstock paper. Nothing special here about the dimensions or materials.

On the front of the card, use either the logos that I am providing, or do some slight modifications to these logos to fit the design that looks the best. Feel free to pick the one that you like, or that will fit what you're trying to do the best here. Take artistic liberty to make this card pop. I do not want any contact information on the front of the card, only the company logo.

On the back of the card I would like the contact information. Please use fictitious contact information for now, and make the background look cool somehow.

```html
<!DOCTYPE html>
<html lang="en">
<head>
<meta charset="utf-8">
<title>Quorvane Works – Business Cards</title>
<link rel="stylesheet" href="https://fonts.googleapis.com/css2?family=Russo+One&family=Cinzel:wght@600&family=Roboto+Slab:wght@600&display=swap">
<style>
  :root {
    --stage: #4a4a4a;
    --orange: #ff4a0d;
    --ink: #1c1c1c;
    --paper: #ffffff;
    --contact-blue: #4a93dc;
    --muted: #e6e6e6;
  }
  html, body {
    margin: 0;
    width: 1200px;
    height: 665px;
    overflow: hidden;
    background: var(--stage);
  }
  .sheet { position: relative; width: 1200px; height: 665px; }
  .card {
    position: absolute;
    width: 411px;
    height: 236px;
    display: block;
    box-shadow: 0 1px 3px rgba(0,0,0,.35);
  }
  .card--back-orange  { left: 103px; top: 85px; }
  .card--back-white   { left: 563px; top: 83px; }
  .card--front-dark   { left: 100px; top: 337px; }
  .card--front-orange { left: 567px; top: 340px; }

  .wordmark { font-family: "Russo One", sans-serif; letter-spacing: 1px; }
  .holder-name { font-family: "Cinzel", serif; font-weight: 600; letter-spacing: 1.6px; }
  .contact { font-family: "Roboto Slab", serif; font-weight: 600; }
  .fill-orange { fill: var(--orange); }
  .fill-ink { fill: var(--ink); }
  .fill-paper { fill: var(--paper); }
  .fill-blue { fill: var(--contact-blue); }
  .fill-muted { fill: var(--muted); }
</style>
</head>
<body>
<main class="sheet">

  <!-- Back, orange panel -->
  <svg class="card card--back-orange" viewBox="0 0 308 177" role="group" aria-label="Card back with contact details">
    <rect class="fill-ink" width="308" height="177"/>
    <polygon class="fill-paper" points="128,0 308,0 308,88 166,88"/>
    <polygon class="fill-orange" points="0,0 128,0 166,88 155,177 0,177"/>
    <g class="wordmark fill-paper" text-anchor="middle">
      <text x="76" y="76" font-size="19">QUORVANE</text>
      <text x="76" y="104" font-size="19">WORKS</text>
    </g>
    <text class="holder-name fill-ink" x="283" y="79" font-size="13" text-anchor="end">DELLAN VARSE</text>
    <g class="contact" text-anchor="end">
      <text class="fill-blue" x="284" y="112" font-size="8">X-XYZ-ABC-1234</text>
      <text class="fill-blue" x="284" y="129" font-size="8">X-XYZ-ABC-1234</text>
      <text class="fill-muted" x="284" y="145" font-size="5.5">3RD ABC RR XYZ, XYZ1223 , XYZ MNO</text>
      <text class="fill-blue" x="284" y="162" font-size="5.5">dellanvarse@quorvaneworks.com</text>
    </g>
    <g class="icons">
      <polygon class="fill-orange" points="290,109.5 293,104 299,104 302,109.5 299,115 293,115"/>
      <rect class="fill-paper" x="293.5" y="107.5" width="5" height="4" rx="1"/>
      <polygon class="fill-orange" points="290,126.5 293,121 299,121 302,126.5 299,132 293,132"/>
      <rect class="fill-paper" x="293.5" y="124.5" width="5" height="4" rx="1"/>
      <polygon class="fill-orange" points="290,143 293,137.5 299,137.5 302,143 299,148.5 293,148.5"/>
      <rect class="fill-paper" x="293" y="140.5" width="6" height="4.5"/>
      <polygon class="fill-orange" points="290,160 293,154.5 299,154.5 302,160 299,165.5 293,165.5"/>
      <circle class="fill-paper" cx="296" cy="159" r="2.2"/>
    </g>
  </svg>

  <!-- Back, white panel -->
  <svg class="card card--back-white" viewBox="0 0 308 177" role="group" aria-label="Card back with contact details">
    <rect class="fill-ink" width="308" height="177"/>
    <polygon class="fill-orange" points="123,0 308,0 308,90 162,90"/>
    <polygon class="fill-paper" points="0,0 123,0 162,90 150,177 0,177"/>
    <g class="wordmark fill-ink" text-anchor="middle">
      <text x="76" y="80" font-size="19">QUORVANE</text>
      <text x="76" y="108" font-size="19">WORKS</text>
    </g>
    <text class="holder-name fill-ink" x="302" y="78" font-size="13" text-anchor="end">DELLAN VARSE</text>
    <g class="contact" text-anchor="end">
      <text class="fill-blue" x="282" y="112" font-size="8">X-XYZ-ABC-1234</text>
      <text class="fill-blue" x="282" y="129" font-size="8">X-XYZ-ABC-1234</text>
      <text class="fill-muted" x="282" y="145" font-size="5.5">3RD ABC RR XYZ, XYZ1223 , XYZ MNO</text>
      <text class="fill-blue" x="282" y="162" font-size="5.5">dellanvarse@quorvaneworks.com</text>
    </g>
    <g class="icons">
      <polygon class="fill-orange" points="288,109.5 291,104 297,104 300,109.5 297,115 291,115"/>
      <rect class="fill-paper" x="291.5" y="107.5" width="5" height="4" rx="1"/>
      <polygon class="fill-orange" points="288,126.5 291,121 297,121 300,126.5 297,132 291,132"/>
      <rect class="fill-paper" x="291.5" y="124.5" width="5" height="4" rx="1"/>
      <polygon class="fill-orange" points="288,143 291,137.5 297,137.5 300,143 297,148.5 291,148.5"/>
      <rect class="fill-paper" x="291" y="140.5" width="6" height="4.5"/>
      <polygon class="fill-orange" points="288,160 291,154.5 297,154.5 300,160 297,165.5 291,165.5"/>
      <circle class="fill-paper" cx="294" cy="159" r="2.2"/>
    </g>
  </svg>

  <!-- Front, dark over orange -->
  <svg class="card card--front-dark" viewBox="0 0 308 177" role="group" aria-label="Card front with company name">
    <rect class="fill-orange" width="308" height="177"/>
    <rect class="fill-ink" width="308" height="88"/>
    <g class="wordmark" text-anchor="middle" font-size="26">
      <text class="fill-orange" x="154" y="76">QUORVANE</text>
      <text class="fill-ink" x="154" y="128">WORKS</text>
    </g>
  </svg>

  <!-- Front, orange over dark -->
  <svg class="card card--front-orange" viewBox="0 0 308 177" role="group" aria-label="Card front with company name">
    <rect class="fill-ink" width="308" height="177"/>
    <rect class="fill-orange" width="308" height="93"/>
    <g class="wordmark" text-anchor="middle" font-size="26">
      <text class="fill-ink" x="154" y="76">QUORVANE</text>
      <text class="fill-orange" x="154" y="130">WORKS</text>
    </g>
  </svg>

</main>
</body>
</html>
```